Flyer to acquire new customers for a craft business

Create an A5 (4 pages in total) flyer describing proposed services from a craft business to new customers.

Services are :

All types of renovation (painting, plastering, attaching wallpapers ....)
All types of repairs
Electric repairs
Little to medium woodworks
Services around the house and garden

Flyer must be translatable into several languages beginning with FRENCH.
Texts are being written by ourselves.

Target Market(s)

Private customers

Industry/Entity Type

Mixed craft business

Colors

Designer to choose colors to be used in the design.

```html
<!DOCTYPE html>
<html lang="fr">
<head>
<meta charset="utf-8">
<title>Bastelhaus – Flyer artisanat</title>
<link rel="stylesheet" href="https://fonts.googleapis.com/css2?family=Montserrat:wght@400;500;600;700;800&display=swap">
<style>
  :root{
    --navy:#2e2850;
    --gold:#e8b95a;
    --gold-light:#f1d49a;
    --cream:#fbf0e0;
    --white:#ffffff;
    --ink:#2f2f3a;
    --ink-soft:#4a4a55;
    --backdrop:#e9e7e3;
  }
  *{box-sizing:border-box;margin:0;padding:0}
  html,body{width:1200px;height:1200px;overflow:hidden;background:var(--backdrop)}
  body{font-family:"Montserrat",sans-serif;position:relative}
  .spread{position:absolute;left:190px;width:1144px;height:811px;transform-origin:0 0;transform:scale(.7168);overflow:hidden;box-shadow:0 4px 18px rgba(0,0,0,.12)}
  .spread--cover{top:12px}
  .spread--inside{top:603px}
  .page{position:absolute;top:0;width:572px;height:811px;overflow:hidden}
  .page--left{left:0}
  .page--right{left:572px}
  .abs{position:absolute}
  svg.layer{position:absolute;left:0;top:0}

  /* brand */
  .brand{position:absolute;display:flex;align-items:center;gap:14px;color:var(--navy);font-weight:800;letter-spacing:.5px}
  .brand__dot{width:22px;height:22px;border-radius:50%;background:var(--gold)}
  .brand--cover{left:0;right:0;top:62px;justify-content:center;font-size:38px}
  .brand--back{left:330px;top:700px;font-size:28px}

  /* back cover */
  .pitch{left:19px;top:476px;width:256px;height:262px;border:7px solid var(--gold);background:var(--white);padding:13px 6px 0 14px;white-space:nowrap}
  .pitch__title{font-weight:700;font-size:15.5px;line-height:22px;color:var(--ink);margin-bottom:7px;letter-spacing:-.1px}
  .pitch__item{font-size:15px;line-height:22px;color:var(--ink-soft);margin-bottom:6px;letter-spacing:-.1px}
  .pitch__notch{position:absolute;right:-34px;top:98px}
  .contacts{left:324px;top:552px;list-style:none}
  .contacts li{display:flex;align-items:center;gap:9px;font-size:14.5px;font-weight:700;color:var(--navy);height:25px}
  .contacts svg{width:13px;height:13px}

  /* cover */
  .cover-title{left:0;right:0;top:158px;text-align:center;font-weight:800;color:var(--navy);font-size:63px;line-height:60px;letter-spacing:.5px}
  .cover-services{left:0;right:0;top:640px;text-align:center;color:var(--gold);font-weight:800;font-size:21px;line-height:45px}

  /* inside */
  .label{position:absolute;font-weight:700;color:var(--navy);font-size:25px}
  .label__band{position:absolute;background:var(--gold);transform:skewX(-12deg) rotate(-4deg)}
  .copy{position:absolute;font-size:15px;line-height:21px;color:var(--ink-soft)}
  .copy p{margin-bottom:6px}
  .copy--light{color:var(--white);font-size:16px;line-height:22px}
  .copy--light p{margin-bottom:10px}
  .elec-title{left:26px;top:24px;font-weight:700;font-size:25px;line-height:28px;color:var(--navy)}
  .elec-copy{left:26px;top:108px;width:256px;font-size:15px;line-height:21px;color:var(--ink)}
</style>
</head>
<body>

<!-- Outer spread: back cover + front cover -->
<section class="spread spread--cover">
  <div class="page page--left" style="background:var(--cream)">
    <svg class="layer" width="572" height="811" viewBox="0 0 572 811">
      <defs>
        <linearGradient id="woodshop" x1="0" y1="0" x2="1" y2="1">
          <stop offset="0" stop-color="#9b7a5a"/>
          <stop offset=".5" stop-color="#c79a6e"/>
          <stop offset="1" stop-color="#d9bfa0"/>
        </linearGradient>
      </defs>
      <polygon points="0,787 240,787 572,585 572,787" fill="var(--white)"/>
      <polygon role="img" aria-label="Photo d'un atelier de menuiserie avec des planches de bois empilées" points="0,0 572,0 572,355 410,450 0,450" fill="url(#woodshop)"/>
      <rect x="0" y="787" width="572" height="24" fill="var(--navy)"/>
      <rect x="311" y="787" width="261" height="7" fill="var(--gold)"/>
    </svg>

    <div class="abs pitch">
      <p class="pitch__title">Vous êtes à la recherche<br>d'un partenaire fiable ?</p>
      <p class="pitch__item">Pour tous types de travaux<br>et de services de l'artisanat</p>
      <p class="pitch__item">Petits, moyens ou plus<br>grands projets</p>
      <p class="pitch__item">Intervention rapide</p>
      <p class="pitch__item">Contactez-nous pour un<br>conseil personnalisé</p>
      <svg class="pitch__notch" width="34" height="44" viewBox="0 0 34 44">
        <polygon points="0,0 30,22 0,44" fill="var(--white)" stroke="var(--gold)" stroke-width="7" stroke-linejoin="miter"/>
        <rect x="-4" y="4" width="4" height="36" fill="var(--white)"/>
      </svg>
    </div>

    <ul class="abs contacts">
      <li><svg viewBox="0 0 16 16"><circle cx="8" cy="8" r="8" fill="var(--navy)"/><path d="M5 4.5l1.5-.5 1 2-1 .8a5 5 0 0 0 2.7 2.7l.8-1 2 1-.5 1.5c-3.5.3-6.8-3-6.5-6.5z" fill="var(--white)"/></svg>+352 20 00 00 00</li>
      <li><svg viewBox="0 0 16 16" fill="none" stroke="var(--navy)" stroke-width="1.4"><circle cx="8" cy="8" r="7"/><ellipse cx="8" cy="8" rx="3" ry="7"/><line x1="1" y1="8" x2="15" y2="8"/></svg>www.bastelhaus.lu</li>
      <li><svg viewBox="0 0 16 16"><rect x="0" y="2" width="16" height="12" fill="var(--navy)"/><path d="M0 2l8 7 8-7M0 14l6-6M16 14l-6-6" stroke="var(--white)" stroke-width="1.3" fill="none"/></svg>info@bastelhaus.lu</li>
    </ul>

    <div class="brand brand--back"><span class="brand__dot"></span>Bastelhaus</div>
  </div>

  <div class="page page--right" style="background:var(--white)">
    <svg class="layer" width="572" height="811" viewBox="0 0 572 811">
      <defs>
        <linearGradient id="paint" x1="0" y1="0" x2="1" y2="1">
          <stop offset="0" stop-color="#c98d4e"/>
          <stop offset=".5" stop-color="#e9dcc2"/>
          <stop offset="1" stop-color="#f0b530"/>
        </linearGradient>
        <linearGradient id="tools" x1="0" y1="0" x2="1" y2="1">
          <stop offset="0" stop-color="#3a3a40"/>
          <stop offset=".5" stop-color="#c9a98e"/>
          <stop offset="1" stop-color="#1f1f24"/>
        </linearGradient>
      </defs>
      <g stroke="var(--gold)" stroke-linecap="butt">
        <line x1="0" y1="695" x2="572" y2="320" stroke-width="22"/>
        <line x1="0" y1="650" x2="572" y2="275" stroke-width="20" opacity=".9"/>
        <line x1="0" y1="605" x2="572" y2="230" stroke-width="18" opacity=".8"/>
        <line x1="0" y1="562" x2="572" y2="187" stroke-width="15" opacity=".6"/>
        <line x1="0" y1="522" x2="572" y2="147" stroke-width="12" opacity=".45"/>
        <line x1="0" y1="485" x2="572" y2="110" stroke-width="9" opacity=".3"/>
        <line x1="0" y1="452" x2="572" y2="77" stroke-width="6" opacity=".2"/>
      </g>
      <polygon points="0,740 572,360 572,811 0,811" fill="var(--navy)"/>
      <polygon role="img" aria-label="Photo de matériel de peinture : rouleaux, pinceaux et gants" points="169,370 286,438 286,573 169,640 52,573 52,438" fill="url(#paint)" stroke="var(--white)" stroke-width="8"/>
      <polygon role="img" aria-label="Photo d'une main tenant une clé plate devant une boîte à outils" points="402,297 523,367 523,507 402,577 281,507 281,367" fill="url(#tools)" stroke="var(--white)" stroke-width="8"/>
    </svg>
    <div class="brand brand--cover"><span class="brand__dot"></span>Bastelhaus</div>
    <h1 class="abs cover-title">Ären<br>Handwierker</h1>
    <div class="abs cover-services">
      <p>Rénovations</p>
      <p>Réparations</p>
      <p>Tous types de services de l'artisanat</p>
    </div>
  </div>
</section>

<!-- Inner spread -->
<section class="spread spread--inside">
  <div class="page page--left" style="background:var(--navy)">
    <div class="abs" role="img" aria-label="Photo d'une pièce en rénovation, moitié en chantier avec échelle, moitié terminée avec sol en marbre et suspensions" style="left:0;top:0;width:572px;height:526px;background:linear-gradient(120deg,#b9b2a6 0%,#d8cdb4 45%,#efe8d8 70%,#e6e2dc 100%)"></div>
    <div class="label__band" style="left:14px;top:498px;width:300px;height:48px"></div>
    <h2 class="label" style="left:44px;top:506px">Rénovations</h2>
    <div class="copy copy--light" style="left:66px;top:582px;width:460px">
      <p>Nous proposons tous types de rénovations (petite, moyenne ou grande envergure)</p>
      <p>Peinture, carrelage, plâtrage, murs en placo-plâtre, sanitaire</p>
      <p>Nous utilisons des produits standards bien connus mais de même des produits naturels comme l'argile et bien d'autres</p>
    </div>
  </div>

  <div class="page page--right" style="background:var(--white)">
    <div class="abs" role="img" aria-label="Photo d'un artisan agenouillé retirant un carrelage au marteau" style="left:19px;top:20px;width:533px;height:294px;background:linear-gradient(110deg,#f2e6d2 0%,#e7d3b4 45%,#8f8a86 75%,#d59a4a 100%)"></div>
    <div class="label__band" style="left:16px;top:290px;width:250px;height:46px"></div>
    <h2 class="label" style="left:50px;top:297px">Réparations</h2>
    <div class="copy" style="left:50px;top:356px;width:200px">
      <p>Une fuite d'eau ? un remplacement d'un tuyau ou même une extension sanitaire ?</p>
      <p>Remplacer du carrelage défectueux même des petits travaux ?</p>
    </div>
    <div class="copy" style="left:291px;top:356px;width:220px">
      <p>Une réparation d'un garde-corps ?</p>
      <p>Le remplacement d'une porte intérieure ?</p>
      <p>Presque tout est possible !</p>
    </div>

    <div class="abs" role="img" aria-label="Photo de mains installant une prise électrique au tournevis" style="left:0;top:526px;width:262px;height:285px;background:linear-gradient(135deg,#d8d6d2 0%,#c9a48a 50%,#e4e6ea 100%)"></div>
    <div class="abs" style="left:262px;top:526px;width:310px;height:285px;background:var(--gold)">
      <h2 class="abs elec-title">Travaux en<br>électricité</h2>
      <p class="abs elec-copy">Installation de lampadaires, remplacements et extensions de circuits électriques, dépannages en électricité, systèmes d'alarme et de vidéo-surveillance ne sont quelques exemples de notre savoir faire</p>
    </div>
  </div>
</section>

</body>
</html>
```